Flyer Design for Upcoming Baseball Clinics, Camps, and Academies

What We Need:
We are looking for a design template we can use for our upcoming sports camps, clinics, and academies. We do elite level training with youth to professional athletes and brand awareness is our number one concern right now.

Ideally this template can be used across multiple sports. Here is our premise:

Clinics (1-Day Event to attract 50+ Athletes)
Camps (2-4 Day Events looking to attract 100+)
Academies (More intimate and skill specific. lasts 6-8 weeks. 10-20 athletes)

Our plan is to do this for Baseball, Football, Basketball, and Lacrosse.

The ideal situation is to be able to use this as a template so we can just edit the document in the future.

Target Market(s)

Prep: Middle School Athletes / ELITE: High School Athletes

Industry/Entity Type

Training

Requirements
Must have
• Things to include:
• Logo, Dates, Times, Investment, Description, Benefits, our mission statement, etc. Our specific colors, specific font family (Bunken Tech Sans Wide), follow our branding deck which is attached.
• Info:
• K7Z BASEBALL CLINIC
• Date: November 11th, 2017
• AGES: PREP: (5th to 8th Grade). ELITE (9th-12th Grade)
• Registration: 8:00am - 9:00 am / 11:00 am - Noon
• Times:
• PREP: 9:00am - 11:00 am
• ELITE: Noon - 2pm
• Investment: $199
• Current Members: $99
Nice to have
• It would be nice to see our mission statement tied in somehow in a unique way. Also maybe a testimonial or two from our pro athletes??
Should not have
• Fake Images: Any Image used needs to be real and give off an authentic feel of a baseball player and the culture.

```html
<!DOCTYPE html>
<html lang="en">
<head>
<meta charset="utf-8">
<title>K7Z Baseball Clinic Flyer</title>
<link href="https://fonts.googleapis.com/css2?family=Stardos+Stencil:wght@700&family=Michroma&display=swap" rel="stylesheet">
<style>
  :root {
    --backdrop: #d9d9d9;
    --paper: #ffffff;
    --ink: #111111;
    --violet: #5d69c4;
    --violet-soft: #7c86d4;
    --stripe-dark: #161616;
    --stripe-grey: #4a4a4a;
  }
  html, body {
    margin: 0;
    padding: 0;
    width: 1041px;
    height: 1200px;
    overflow: hidden;
    background: var(--backdrop);
  }
  .flyer {
    position: absolute;
    left: 101px;
    top: 6px;
    width: 762px;
    height: 1080px;
    background: var(--paper);
    transform: scale(1.1);
    transform-origin: top left;
    overflow: hidden;
  }
  .flyer-art {
    position: absolute;
    inset: 0;
    width: 762px;
    height: 1080px;
  }
  .brand {
    position: absolute;
    left: 56px;
    top: 540px;
    display: flex;
    align-items: center;
    gap: 10px;
  }
  .brand-square {
    width: 14px;
    height: 14px;
    background: var(--ink);
  }
  .brand-name {
    font-family: "Michroma", sans-serif;
    font-size: 15px;
    letter-spacing: 2px;
    color: var(--ink);
  }
  .event-title {
    position: absolute;
    left: 40px;
    top: 690px;
    width: 300px;
    margin: 0;
    text-align: center;
    font-family: "Stardos Stencil", sans-serif;
    font-weight: 700;
    font-size: 34px;
    line-height: 40px;
    color: var(--ink);
  }
  .event-subtitle {
    position: absolute;
    left: 50px;
    top: 778px;
    margin: 0;
    font-family: "Michroma", sans-serif;
    font-size: 13.5px;
    color: var(--ink);
  }
  .event-details {
    position: absolute;
    left: 48px;
    top: 814px;
    margin: 0;
    padding: 0;
    list-style: none;
    font-family: "Michroma", sans-serif;
    font-size: 10.6px;
    line-height: 15.3px;
    color: var(--ink);
  }
</style>
</head>
<body>
  <main class="flyer">
    <svg class="flyer-art" viewBox="0 0 762 1080" xmlns="http://www.w3.org/2000/svg">
      <defs>
        <linearGradient id="fieldTones" x1="0" y1="0" x2="0" y2="1">
          <stop offset="0" stop-color="#1b2030"/>
          <stop offset="0.45" stop-color="#2e3244"/>
          <stop offset="0.62" stop-color="#6f8f4f"/>
          <stop offset="0.82" stop-color="#5c8a44"/>
          <stop offset="0.9" stop-color="#b55a3c"/>
          <stop offset="1" stop-color="#a44d33"/>
        </linearGradient>
        <radialGradient id="ballTones" cx="0.5" cy="0.5" r="0.5">
          <stop offset="0" stop-color="#f2efe8"/>
          <stop offset="1" stop-color="#8c8477"/>
        </radialGradient>
      </defs>

      <rect class="hero-photo" role="img" aria-label="Photo of a batter in a white pinstripe uniform and blue helmet squaring to bunt on a baseball field" x="0" y="0" width="762" height="800" fill="url(#fieldTones)"/>

      <path class="paper-wave" d="M0 365 C120 360 230 420 320 560 C410 700 480 790 640 792 C700 792 740 780 762 760 L762 1080 L0 1080 Z" fill="var(--paper)"/>
      <path class="wave-band" d="M150 360 C235 380 285 450 330 545 C420 700 490 778 640 780 C700 780 740 768 762 748" fill="none" stroke="var(--violet-soft)" stroke-width="20" opacity="0.9"/>

      <g class="accent-stripes" fill="var(--violet)">
        <polygon points="20,258 130,270 134,290 24,278"/>
        <polygon points="0,288 150,300 153,318 0,306"/>
        <polygon points="0,318 170,330 172,346 0,334"/>
        <polygon points="60,348 175,356 176,372 62,366"/>
        <polygon points="70,378 130,384 132,408 72,402"/>
        <polygon points="100,380 165,386 165,400 100,396"/>
      </g>

      <g class="speed-stripes">
        <polygon points="640,802 672,802 620,930 588,930" fill="var(--violet)"/>
        <polygon points="690,780 725,780 650,1000 615,1000" fill="var(--stripe-dark)"/>
        <polygon points="735,752 762,752 762,790 690,1020 655,1020" fill="var(--stripe-dark)"/>
        <polygon points="700,930 740,930 690,1080 650,1080" fill="var(--stripe-grey)"/>
        <polygon points="745,940 762,940 762,1000 735,1080 715,1080" fill="var(--stripe-dark)"/>
        <polygon points="620,930 660,930 630,1020 595,1020" fill="var(--stripe-grey)"/>
      </g>
      <rect class="baseball-photo" role="img" aria-label="Close-up photo of a baseball with red stitching" x="680" y="790" width="82" height="140" fill="url(#ballTones)"/>
    </svg>

    <div class="brand">
      <span class="brand-square"></span>
      <span class="brand-name">K7Z TRAINING HOUSE</span>
    </div>

    <h1 class="event-title">K7Z BASEBALL CLINIC</h1>
    <p class="event-subtitle">Personal &amp; Team Training</p>

    <ul class="event-details">
      <li>Date: November 11th, 2017</li>
      <li>AGES: PREP: (5th to 8th Grade).</li>
      <li>ELITE (9th-12th Grade)</li>
      <li>Registration: 8:00am - 9:00 am/</li>
      <li>11:00 am - Noon</li>
      <li>Times:</li>
      <li>PREP: 9:00am - 11:00 am</li>
      <li>ELITE: Noon - 2pm</li>
      <li>Investment: $199</li>
      <li>Current Members: $99</li>
    </ul>
  </main>
</body>
</html>
```